Velvetorchid Hair & Beauty Business Card

Velvetorchid Hair & Beauty is a boutique salon located in the picturesque Lake Taupo NZ. The salon is very luxurious, opulent gold gilded mirrors, chandelier lit, contemporary french decor, sets the mood to create beautiful hair, makeup and all beauty services. Just had a new logo design and now after a new business card.
Logo
14 Korowhai Street
Taupo
Phone (07) 548 6193
www.velvetorchid.co.nz
email hair@velvetorchid.co.nz
Marlena Swithin
Also need a space to put in Stylist name, date, appointment time. thanks;)
Another idea is we could incorporate the wallpaper in the back ground either on the back or front or use an ornate glided frame (around the edge of the card) like on my website where my brides photos flash.
Decided against the wall paper but at least you can see our colour theme for the salon.
Updates

Please check out my updated brief . Thanks :)

Target Market(s)

25-60 years plus, mainly mid age females , wanting the best possible service , high standard of workmanship and money not a problem.

Industry/Entity Type

Boutique

Requirements
Must have
• Gold and silver

```html
<!DOCTYPE html>
<html lang="en">
<head>
<meta charset="utf-8">
<title>Velvetorchid Hair &amp; Beauty – Business Card</title>
<link rel="stylesheet" href="https://fonts.googleapis.com/css2?family=Didact+Gothic&display=swap">
<style>
  :root {
    --backdrop: #2f2f30;
    --cream-light: #f4ecca;
    --cream-deep: #e8d9a6;
    --paper-white: #f8f6f0;
    --gold: #a88a3c;
    --silver: #6e6e74;
    --ink-grey: #55555a;
    --dots: #8a8170;
  }
  * { box-sizing: border-box; margin: 0; padding: 0; }
  html, body {
    width: 1200px; height: 803px; overflow: hidden;
    background: var(--backdrop);
    font-family: "Didact Gothic", "Century Gothic", sans-serif;
  }
  .stage {
    width: 1200px; height: 803px;
    display: flex; align-items: center; justify-content: center; gap: 48px;
  }
  .card {
    width: 525px; height: 300px; position: relative;
    box-shadow: 0 14px 30px rgba(0,0,0,.45);
  }
  .card--appointment { background: linear-gradient(135deg, var(--cream-light), var(--cream-deep)); }
  .card--contact { background: var(--paper-white); }

  .brand-name {
    position: absolute; left: 40px; top: 92px; right: 40px;
    font-size: 30px; line-height: 1.2; font-weight: 400;
    color: var(--silver); white-space: nowrap;
  }

  .appointment-fields {
    position: absolute; left: 40px; top: 178px; right: 40px;
    font-size: 13px; color: var(--ink-grey); line-height: 2.2;
  }
  .field-row { display: flex; gap: 8px; }
  .field { display: flex; align-items: baseline; flex: 1; white-space: nowrap; }
  .field__blank {
    flex: 1; border-bottom: 1px dotted var(--dots); margin-left: 6px; height: 1em;
  }
  .field--date { flex: 0 0 150px; }

  .contact {
    position: absolute; left: 40px; top: 172px; right: 30px;
    color: var(--ink-grey); font-size: 12.5px; line-height: 1.75;
  }
  .contact__person { color: var(--gold); font-size: 17px; letter-spacing: .5px; margin-bottom: 4px; }
  .contact__label { color: var(--gold); }
  .contact__line span + span { margin-left: 12px; }
</style>
</head>
<body>
<main class="stage">
  <section class="card card--appointment" aria-label="Appointment card">
    <p class="brand-name">Velvetorchid Hair &amp; Beauty</p>
    <div class="appointment-fields">
      <div class="field-row">
        <div class="field">Stylist name:<span class="field__blank"></span></div>
        <div class="field field--date">Date:<span class="field__blank"></span></div>
      </div>
      <div class="field-row">
        <div class="field">Appointment time:<span class="field__blank"></span></div>
      </div>
    </div>
  </section>

  <section class="card card--contact" aria-label="Contact card">
    <p class="brand-name">Velvetorchid Hair &amp; Beauty</p>
    <div class="contact">
      <p class="contact__person">Marlena Swithin</p>
      <p class="contact__line">14 Korowhai Street, Taupo</p>
      <p class="contact__line"><span><span class="contact__label">p:</span> (07) 548 6193</span><span><span class="contact__label">e:</span> hair@velvetorchid.co.nz</span></p>
      <p class="contact__line"><span class="contact__label">w:</span> www.velvetorchid.co.nz</p>
    </div>
  </section>
</main>
</body>
</html>
```